Speakwright election of District 71 Club Growth Director.

This is a tri-fold brochure. I have a basic layout from last years election but would like to add some detail and punch to the campaign brochure. I have a sample from last year. I've also included a sample of a brochure with some depth and personality. The design should communicate that I am a transformational leader who has a solid foundation in helping others to build a better Speakwright experience. If you have the winning design I will need business cards, post cards, and a poster.

Target Market(s)

Speakwright leaders with in Georgia. 25 yrs to 64 yrs = 80% of membership; 51% are female, over 75% have at least a Bachelor's degree or higher; 40% are specialist and 24% managers; 27% earn $100,000 or more - 41% earn $75,000 per year.

Industry/Entity Type

Non-Profit

Font styles to use
Sans Serif

Requirements
Must have
• Professional look. Playing off my experience as a residential contractor. Nickname is "iron boot" Morlow.
Nice to have
• larger font
Should not have
• Can not be hard to read

```html
<!DOCTYPE html>
<html lang="en">
<head>
<meta charset="utf-8">
<title>Vote Dana Morlow – Club Growth Director</title>
<link rel="stylesheet" href="https://fonts.googleapis.com/css2?family=Anton&family=Oswald:wght@400;500;600;700&family=Open+Sans:wght@400;600;700&display=swap">
<style>
:root{
  --bg:#6b4a14;
  --black:#0b0b0b;
  --ink:#0d0d0d;
  --orange:#d9861a;
  --amber:#f0a526;
  --deep:#a9570d;
  --yellow:#f7d417;
  --white:#ffffff;
  --photo:#cfc6bd;
}
*{box-sizing:border-box;margin:0;padding:0}
html,body{width:900px;height:1200px;overflow:hidden;background:var(--bg)}
body{position:relative;font-family:"Open Sans",Arial,sans-serif;color:var(--white)}
.sheet{position:absolute;left:150px;width:600px;background:var(--black);overflow:hidden}
.sheet--inside{top:80px;height:475px}
.sheet--outside{top:648px;height:465px}
.abs{position:absolute}
.caution-band{position:absolute;background:var(--yellow)}
.photo{position:absolute;background:linear-gradient(160deg,#e8e2da,var(--photo) 60%,#8a7b6c)}

/* inside sheet */
.inside-left{position:absolute;left:0;top:0;width:195px;height:475px}
.future{position:absolute;left:0;top:224px;width:195px;height:228px;background:linear-gradient(135deg,var(--amber),var(--orange));clip-path:polygon(0 7%,100% 0,100% 100%,0 100%);padding:24px 12px 0 16px}
.future h2{font-family:"Oswald",Arial,sans-serif;font-weight:600;font-size:15px;color:var(--black);margin-bottom:8px}
.future p{font-size:8.2px;font-weight:600;line-height:1.35;color:var(--ink);margin-bottom:7px}
.title{position:absolute;left:222px;top:62px;width:350px;text-align:center;font-family:"Anton",Impact,sans-serif;line-height:.98;text-shadow:3px 3px 0 #3b2204}
.title .l1{font-size:56px;color:var(--orange)}
.title .l2{font-size:56px;color:var(--yellow)}
.of-year{position:absolute;left:195px;top:214px;width:405px;text-align:center;font-family:"Oswald",Arial,sans-serif;font-weight:700;font-size:14px;color:var(--yellow)}
.of-year span{color:var(--white)}
.role{position:absolute;width:146px}
.role h3{font-family:"Oswald",Arial,sans-serif;font-weight:500;font-size:11px;color:var(--yellow);margin-bottom:2px}
.role p{font-size:6px;line-height:1.3;color:#f2f2f2}
.badge{position:absolute;width:40px;height:40px;background:#d8d8d8;border-radius:2px}
.badge--round{border-radius:50%;background:#3a4a66}
.badge--dark{background:#555}

/* outside sheet */
.meet{position:absolute;left:22px;top:58px;width:160px;height:20px;border-radius:10px;background:var(--amber);color:var(--black);font-family:"Oswald",Arial,sans-serif;font-weight:600;font-size:11px;text-align:center;line-height:20px}
.bio{position:absolute;left:14px;top:84px;width:178px}
.bio h3{font-family:"Oswald",Arial,sans-serif;font-weight:500;font-size:12px;color:var(--amber);margin:3px 0 2px}
.bio h4{font-family:"Oswald",Arial,sans-serif;font-weight:400;font-size:10px;color:var(--amber);margin-bottom:2px}
.bio ul{list-style:none}
.bio li{position:relative;padding-left:10px;font-size:6.6px;font-weight:600;line-height:1.3;margin-bottom:3px;color:var(--white)}
.bio li::before{content:"";position:absolute;left:0;top:2px;width:5px;height:5px;background:var(--amber)}
.bio p{font-size:6.6px;font-weight:600;line-height:1.3;padding-left:10px;margin-bottom:3px}
.quote{position:absolute;left:210px;top:28px;width:182px;text-align:center;font-family:"Oswald",Arial,sans-serif;font-weight:500;font-size:10px;line-height:1.3;color:var(--yellow)}
.goals{position:absolute;left:210px;top:116px;width:182px}
.goals h3{font-family:"Oswald",Arial,sans-serif;font-weight:600;font-size:15px;color:var(--black);margin-bottom:14px}
.goals ul{list-style:none}
.goals li{position:relative;padding-left:10px;font-size:7.2px;font-weight:700;line-height:1.3;color:var(--ink);margin-bottom:8px}
.goals li::before{content:"";position:absolute;left:0;top:2px;width:5px;height:5px;background:var(--white)}
.contact{position:absolute;left:200px;top:362px;width:200px;text-align:center}
.contact .vote{font-family:"Oswald",Arial,sans-serif;font-weight:600;font-size:15px;line-height:1}
.contact .name{font-family:"Oswald",Arial,sans-serif;font-weight:600;font-size:10px;margin-top:2px}
.contact .line{display:flex;align-items:center;justify-content:center;gap:4px;font-size:9.5px;font-weight:600;margin-top:1px}
.contact svg{width:8px;height:8px}
.cover-name{position:absolute;left:400px;top:32px;width:200px;text-align:center;font-family:"Oswald",Arial,sans-serif;font-weight:700;line-height:1}
.cover-name .vote{font-size:32px;color:var(--white)}
.cover-name .who{font-size:30px;background:linear-gradient(90deg,var(--orange),var(--yellow));-webkit-background-clip:text;background-clip:text;color:transparent}
.cover-panel{position:absolute;left:400px;top:150px;width:200px;height:315px;background:linear-gradient(90deg,var(--deep),var(--amber) 60%,var(--orange))}
.for{position:absolute;left:400px;top:172px;width:188px;text-align:right;font-family:"Oswald",Arial,sans-serif;font-weight:500;color:var(--black);line-height:1.15}
.for .a{font-size:20px;padding-right:22px}
.for .b{font-size:20px}
.for .c{font-size:15px;padding-right:18px}
</style>
</head>
<body>

<!-- Inside spread -->
<section class="sheet sheet--inside">
  <div class="inside-left">
    <div class="photo" style="left:20px;top:18px;width:155px;height:200px" role="img" aria-label="Portrait of the candidate in a white hard hat and white blazer"></div>
    <svg class="abs" style="left:170px;top:0" width="40" height="240" viewBox="0 0 40 240"><polygon points="8,0 25,0 25,240 12,240" fill="#d9861a"/></svg>
    <div class="future">
      <h2>Building a Better Future</h2>
      <p>With Speakwright's blueprint for success in hand, I am ready to report to work for you as your Club Growth Director.</p>
      <p>Given the opportunity to serve you, I will parlay the leadership skills gained through Speakwright, in business and as a community leader to build a better future for you.</p>
      <p>It would be a privilege to serve as your Club Growth Director. I appreciate your vote of confidence on May 14, 2016</p>
    </div>
    <div class="caution-band" style="left:0;top:454px;width:210px;height:16px" role="img" aria-label="Caution stripe band"></div>
  </div>

  <svg class="abs" style="left:195px;top:0" width="405" height="60" viewBox="0 0 405 60" role="img" aria-label="Caution stripe band">
    <polygon points="0,24 405,4 405,26 0,48" fill="#f7d417"/>
  </svg>
  <div class="title"><div class="l1">CLUB GROWTH</div><div class="l2">DIRECTOR</div></div>
  <svg class="abs" style="left:240px;top:182px" width="340" height="24" viewBox="0 0 340 24"><polygon points="0,16 180,16 200,2 340,2 340,9 206,9 186,22 0,22" fill="#d9861a"/></svg>
  <div class="of-year">SPEAKWRIGHT <span>OF THE YEAR</span></div>

  <div class="badge" style="left:222px;top:254px"></div>
  <div class="role" style="left:268px;top:240px"><h3>District Leader</h3><p>2015-2016 Division H Director<br>2014-2015 Speakwright of the Year<br>2014-2015 Speakwright of the Year<br>2013-2014 Awards Chair<br>2011-2012 Area Governor<br>2012-2013 Parliamentarian<br>2012-2013 Outstanding Speakwright Award<br>2014 to present Ambassador of Education and Revitalization Program</p></div>

  <div class="badge badge--dark" style="left:222px;top:330px"></div>
  <div class="role" style="left:268px;top:324px"><h3>Speaker</h3><p>2016 Accredited Speakers Workshop Host<br>2015 Fall Conference Workshop<br>2014 Target Speaker District 71's Evaluation Contest<br>2014 Target Speaker District 71's Evaluation Contest</p></div>

  <div class="badge" style="left:222px;top:404px;background:#e6e6f0"></div>
  <div class="role" style="left:268px;top:397px"><h3>Membership</h3><p>2010 to date Sponsor of 36 new members<br>2015 Coaches and Mentors workshop training<br>2012 Charter Member - North Ridge Advanced Speakwrights</p></div>

  <div class="badge badge--round" style="left:404px;top:254px"></div>
  <div class="role" style="left:452px;top:240px"><h3>Conference Leader</h3><p>2014 Spring Conference Co-Chair "Driven by the Voice of Leadership"<br>2013 Spring Conference Vice-chair "Looking Back to the Future"</p></div>

  <div class="badge badge--dark" style="left:404px;top:316px"></div>
  <div class="role" style="left:452px;top:310px"><h3>Chief Judge</h3><p>2016 Revitalized Judges Training<br>2014 &amp; 2010 Certified as Expert Chief Judge<br>2014 Judge Humorously Speaking Contest<br>2013 Judge Table Topics<br>2011 Chief Judge International Speech Contest</p></div>

  <div class="badge" style="left:404px;top:396px;background:#c9b37a"></div>
  <div class="role" style="left:452px;top:382px"><h3>Club Leader</h3><p>2013-2014 President - Lakeside, President's Distinguished Club; 10 of 10 goals<br>2011-2012 Sergeant of Arms — Lakeside, President's Distinguished Club; 10 of 10 goals<br>2015-2016 VP of Membership - North Ridge Advanced Speakwrights<br>VP of Membership</p></div>
</section>

<!-- Outside spread -->
<section class="sheet sheet--outside">
  <svg class="abs" style="left:0;top:0" width="200" height="465" viewBox="0 0 200 465">
    <defs><linearGradient id="amberFade" x1="0" y1="0" x2="1" y2="1"><stop offset="0" stop-color="#f0a526"/><stop offset="1" stop-color="#a9570d"/></linearGradient></defs>
    <rect width="200" height="465" fill="url(#amberFade)"/>
    <polygon points="0,44 200,20 200,28 0,52" fill="#ffffff"/>
    <polygon points="0,52 200,28 200,430 0,410" fill="#0b0b0b"/>
  </svg>
  <div class="meet">MEET DANA MORLOW</div>
  <div class="bio">
    <h3>Personal</h3>
    <ul>
      <li>Married 37 years to Dale Morlow. Two children, youngest, Grant lives in Denver. Nora married to Owen Pratt lives in Johns Creek with two daughters Ella (17) and Josie (16).</li>
      <li>Coastal State University BS in Communications.</li>
      <li>Home Builders Academy.</li>
      <li>Black Belt Taekwondo</li>
    </ul>
    <h3>Business &amp; Professional</h3>
    <h4>40+ years as a business leader</h4>
    <ul>
      <li>CEO of a multi-million dollar international research and development company.</li>
      <li>Operations Director for a $32 million inter-national marketing company of alternative health products</li>
      <li>Award winning Residential Contractor building over $20 million in homes</li>
      <li>WRVN TV News Anchor Montgomery, AL winner of 2 Press Guild Awards for Journalism.</li>
    </ul>
    <h3>Civic Leadership</h3>
    <p>Over the past 36 years Dana has been selected for key leadership roles in more than fifteen organizations including:</p>
    <ul>
      <li>Board of Directors, Atlantic Trade Chamber.</li>
      <li>Board of Directors, Georgia Women of Faith Council.</li>
    </ul>
  </div>

  <svg class="abs" style="left:200px;top:0" width="200" height="465" viewBox="0 0 200 465">
    <defs><linearGradient id="goalFade" x1="0" y1="0" x2="1" y2="0"><stop offset="0" stop-color="#f0a526"/><stop offset="1" stop-color="#d08018"/></linearGradient></defs>
    <polygon points="0,82 200,82 200,330 120,360 0,330" fill="url(#goalFade)"/>
    <polygon points="0,82 130,82 0,130" fill="#e39420"/>
  </svg>
  <div class="quote">"It would be an honor to serve you as your Club Growth Director. I appreciate your vote of confidence."</div>
  <div class="goals">
    <h3>Goals:</h3>
    <ul>
      <li>Grow and strengthen our District 71 Speakwright membership base.</li>
      <li>Lead a strong club-building team to meet our District membership and club-building goals. Stop the leaky bucket syndrome where clubs are losing 50% of their membership each year.</li>
      <li>Support our Division and Area Directors specifically chartering new clubs, member renewals and growing membership.</li>
      <li>Creativity in getting the message out.</li>
      <li>Strengthen the bond between VP of Membership and VP of PR.</li>
    </ul>
  </div>
  <div class="contact">
    <div class="vote">VOTE</div>
    <div class="name">DANA MORLOW DTM</div>
    <div class="line"><svg viewBox="0 0 10 8"><rect x=".5" y=".5" width="9" height="7" fill="none" stroke="#fff"/><polyline points=".5,.5 5,4.5 9.5,.5" fill="none" stroke="#fff"/></svg>dana@morlowvote.com</div>
    <div class="line"><svg viewBox="0 0 10 10"><rect width="10" height="10" rx="2" fill="#fff"/><path d="M3 2.2 L4.2 3.6 L3.6 4.3 Q4.6 5.8 5.8 6.4 L6.4 5.8 L7.8 7 L7 8 Q3.5 7.6 2 3 Z" fill="#0b0b0b"/></svg>555-014-2290</div>
  </div>
  <div class="caution-band" style="left:200px;top:440px;width:200px;height:14px" role="img" aria-label="Caution stripe band"></div>

  <div class="caution-band" style="left:400px;top:4px;width:200px;height:18px" role="img" aria-label="Caution stripe band"></div>
  <div class="cover-name"><div class="vote">VOTE</div><div class="who">DANA<br>MORLOW</div></div>
  <div class="cover-panel"></div>
  <div class="for"><div class="a">FOR</div><div class="b">CLUB GROWTH</div><div class="c">DIRECTOR</div></div>
  <div class="photo" style="left:420px;top:262px;width:170px;height:203px;background:linear-gradient(160deg,#f3efe9,#d8d0c6 55%,#2a2522)" role="img" aria-label="Candidate in white hard hat and blazer presenting with open hands"></div>
</section>

</body>
</html>
```